Environmental Company Website
Kelvro Remediation website
Project: Environmental Company Website
Environmental Company Website - Environment
Creative Brief
Environment
www.kelvroremediation.example
We are an environmental cleanup/spill response company. We service Industrial and Municiple customers. Most of our work revolves around gas/petroleum spills or tank cleaning. We need to keep a very professional, emergency response image. We are not so different than a fire department in our emergency nature. We sell spill supplies to our customers, but we will not sell from our website.
Dislike busy, clumsy, long page websites. Looking for a one page length website (if possible). No scrolling needed to view the pages unless the content demands it. The home page fills the screen, but doesn't go down below the bottom of the window. The nav bar could be on the top or left, whatever best compliments the page.
Elegant
Black / Gray / White/ Blue (see logo)
Yellow
Your choice, we're open to ideas
Arial, Verdana
top
www.lorptank.example
http://www.mavulonsite.example/
http://www.wandertidebreaks.example/
Additional websites we like: http://www.hollisquay-horology.example/en2/ http://www.pinmoorcatch.example/ http://www.oakventhomefit.example/ http://tamworkbuilders.example/ http://www.quennabay.example/ourcatch/

```html
<!DOCTYPE html>
<html lang="en">
<head>
<meta charset="utf-8">
<title>Kelvro Remediation, LLC</title>
<link href="https://fonts.googleapis.com/css2?family=Arimo:wght@400;700&display=swap" rel="stylesheet">
<style>
:root{
  --bg-blue:#1f63b0;
  --bg-blue-dark:#0f3f7c;
  --page:#ffffff;
  --nav-blue:#1e5f8f;
  --nav-active:#4b4b4b;
  --panel-dark:#0d3d78;
  --panel-mid:#2b6fb4;
  --panel-light:#6aa8e0;
  --orange:#e8712a;
  --orange-dark:#b9501a;
  --teal:#2a9a8c;
  --label-green:#1f8a6f;
  --footer:#3b3a39;
  --ink:#1a1a1a;
  --white:#ffffff;
  --muted:#d9d9d9;
}
*{margin:0;padding:0;box-sizing:border-box}
html,body{width:1200px;height:850px;overflow:hidden}
body{
  font-family:"Arimo",Arial,sans-serif;
  background:radial-gradient(ellipse at 50% 40%,var(--bg-blue) 0%,var(--bg-blue-dark) 100%);
  position:relative;
}
.page{position:absolute;left:115px;top:0;width:994px;height:804px;background:var(--page)}
.brand{position:absolute;left:32px;top:58px;font-size:22px;font-weight:700;color:var(--ink);letter-spacing:.5px}
.call{position:absolute;right:42px;top:40px;display:flex;align-items:center;gap:8px;font-size:15px;font-weight:700;color:var(--ink)}
.nav{position:absolute;left:341px;top:113px;width:643px;height:31px;background:var(--nav-blue);display:flex;align-items:stretch}
.nav a{color:var(--white);text-decoration:none;font-size:12.5px;font-weight:700;display:flex;align-items:center;padding:0 15px}
.nav a.active{background:var(--nav-active);color:var(--white);padding:0 34px;border-bottom:3px solid var(--orange)}
.panel{position:absolute;left:5px;top:151px;width:984px;height:533px;
  background:radial-gradient(ellipse at 35% 25%,var(--panel-light) 0%,var(--panel-mid) 35%,var(--panel-dark) 100%)}
.tile{position:absolute;top:12px;height:264px;border:2px solid var(--white)}
.tile .photo{position:absolute;inset:0}
.tile .label{position:absolute;left:14px;top:18px;width:26px;height:160px;background:var(--orange);
  display:flex;align-items:center;justify-content:center}
.tile .label span{transform:rotate(-90deg);white-space:nowrap;font-size:14px;font-weight:700;color:var(--label-green)}
.tile .label b{color:var(--white)}
.contact{position:absolute;left:48px;top:300px;width:221px;height:192px;background:var(--nav-blue);border:2px solid #7fb2de}
.contact h2{height:26px;background:#155085;color:var(--white);font-size:14px;font-weight:700;text-align:center;line-height:26px}
.field{display:block;margin:6px 0 0 20px;width:176px;height:20px;background:var(--white);border:1px solid #999;font-size:13px;color:var(--ink);padding-left:4px;line-height:18px}
.field.message{height:42px}
.submit{display:block;margin:12px auto 0;width:66px;height:22px;background:var(--orange-dark);color:var(--white);font-size:12px;font-weight:700;text-align:center;line-height:20px;border:1px solid #f0c08f}
.welcome{position:absolute;left:283px;top:315px;font-size:17px;font-weight:700;color:var(--white)}
.welcome em{font-style:normal;color:var(--orange)}
.intro{position:absolute;left:283px;top:358px;width:680px;font-size:12.5px;line-height:16px;color:var(--white)}
.more{position:absolute;left:804px;top:432px;width:84px;height:31px;background:var(--orange-dark);border:3px solid var(--teal);
  color:var(--white);font-size:11px;font-weight:700;text-align:center;line-height:25px}
.footer{position:absolute;left:0;top:684px;width:994px;height:101px;background:var(--footer)}
.footer .links{position:absolute;left:48px;top:34px;font-size:11px;color:var(--muted)}
.footer .fbrand{position:absolute;right:40px;top:31px;font-size:13px;font-weight:700;color:var(--white)}
.footer .copy{position:absolute;right:40px;top:66px;font-size:9px;color:var(--muted)}
</style>
</head>
<body>
<div class="page">
  <div class="brand">Kelvro Remediation, LLC</div>
  <div class="call">
    <svg width="16" height="16" viewBox="0 0 24 24" aria-hidden="true"><path fill="#1a1a1a" d="M6.6 10.8c1.4 2.8 3.8 5.1 6.6 6.6l2.2-2.2c.3-.3.7-.4 1-.2 1.1.4 2.3.6 3.6.6.6 0 1 .4 1 1V20c0 .6-.4 1-1 1C10.6 21 3 13.4 3 4c0-.6.4-1 1-1h3.5c.6 0 1 .4 1 1 0 1.3.2 2.5.6 3.6.1.3 0 .7-.2 1z"/></svg>
    CALL US 555-014-2390
  </div>
  <nav class="nav">
    <a class="active" href="#">HOME</a>
    <a href="#">ABOUT US</a>
    <a href="#">SPILL RESPONSES</a>
    <a href="#">EQUIPMENT</a>
    <a href="#">SERVICES</a>
    <a href="#">CONTACT</a>
  </nav>

  <section class="panel">
    <div class="tile" style="left:43px;width:216px">
      <div class="photo" role="img" aria-label="Offshore drilling rig at sea under a blue sky" style="background:linear-gradient(#4d8fd6,#9cc3ea 55%,#3f6f9e 80%,#b84a2a)"></div>
      <div class="label"><span>Chemical <b>Spill</b></span></div>
    </div>
    <div class="tile" style="left:266px;width:219px">
      <div class="photo" role="img" aria-label="White egrets standing in a reedy wetland" style="background:linear-gradient(#c9b27a,#8a9a63 50%,#5d86a8)"></div>
      <div class="label"><span>Petroleum <b>Spill</b></span></div>
    </div>
    <div class="tile" style="left:490px;width:216px">
      <div class="photo" role="img" aria-label="Yellow barrels with radiation and hazard warning signs" style="background:linear-gradient(#6fa8dc,#cfe2f3 55%,#e6c12a)"></div>
      <div class="label"><span>Radiation <b>Spill</b></span></div>
    </div>
    <div class="tile" style="left:713px;width:216px">
      <div class="photo" role="img" aria-label="Crew in protective suits working on a cleanup at the waterfront" style="background:linear-gradient(#9fc4e6,#3f7fb8 50%,#d9d24a)"></div>
      <div class="label"><span>Water <b>Response</b></span></div>
    </div>

    <form class="contact">
      <h2>CONTACT US</h2>
      <span class="field">Name</span>
      <span class="field">E-Mail</span>
      <span class="field message">Message</span>
      <span class="submit">SUBMIT</span>
    </form>

    <h1 class="welcome"><em>Welcome</em> To Our Site !</h1>
    <p class="intro">We are an environmental cleanup/spill response company. We service Industrial and Municiple customers. Most of our work revolves around gas/petroleum spills or tank cleaning. We need to keep a very professional, emergency response image. We are not so different than a fire department in our emergency nature. We sell spill supplies to our customers, but we will not sell from our website.</p>
    <div class="more">READ MORE</div>
  </section>

  <footer class="footer">
    <div class="links">Home| About Us | Spill Respose | Equipment | Services | Clean Up &amp; Responses | Contact</div>
    <div class="fbrand">Kelvro Remediation, LLC</div>
    <div class="copy">© 2013 Kelvro Remediation, LLC. All rights reserved</div>
  </footer>
</div>
</body>
</html>
```